Prescription Savings Card

Looking to revamp our cards that are distributed to pharmacies. Processing information must stand out and be in black with lines through zeros for easy identification.
I have included some previous card designs for consideration. we are looking to go with something cleaner with mainly processing information on the back similar to all white version attached.
Target Market(s)
Pharmacists and Pharmacy Technicians
Industry/Entity Type
prescription medications
Contact Information for Business Card
processing information
Requirements
Must have
- easy to read processing information

```html
<!DOCTYPE html>
<html lang="en">
<head>
<meta charset="UTF-8">
<title>MedPath.com Prescription Savings Card</title>
<link href="https://fonts.googleapis.com/css2?family=Roboto:wght@400;500;700&display=swap" rel="stylesheet">
<style>
  :root {
    --stage: #111111;
    --card: #ffffff;
    --navy: #3a4d80;
    --red: #dc343b;
    --ink: #111111;
    --muted: #8a8a8a;
    --tagline: #5a6a9a;
  }
  * { margin: 0; padding: 0; box-sizing: border-box; }
  html, body { width: 1200px; height: 1000px; overflow: hidden; }
  body {
    background: var(--stage);
    font-family: "Roboto", Arial, sans-serif;
    position: relative;
  }
  .card {
    position: absolute;
    left: 294px;
    width: 613px;
    height: 351px;
    background: var(--card);
    border-radius: 26px;
    overflow: hidden;
  }
  .card-front { top: 149px; }
  .card-back { top: 570px; }
  .card-shapes { position: absolute; inset: 0; width: 613px; height: 351px; }
  .shape-navy { fill: var(--navy); }
  .shape-red { fill: var(--red); }

  .pricing-note {
    position: absolute; left: 42px; top: 100px;
    font-size: 14px; color: var(--muted);
  }
  .brand-name {
    position: absolute;
    font-weight: 700;
    color: var(--navy);
    letter-spacing: -1.5px;
    line-height: 1;
  }
  .card-front .brand-name { left: 40px; top: 145px; font-size: 66px; }
  .tagline {
    position: absolute; left: 41px; top: 218px;
    font-size: 19.5px; color: var(--tagline);
  }

  .card-back .brand-name { left: 79px; top: 76px; font-size: 32px; letter-spacing: -0.8px; }
  .benefits {
    position: absolute; left: 79px; top: 136px;
    list-style: none; font-size: 19px; color: var(--ink); line-height: 24.5px;
  }
  .benefits li::before { content: "• "; }
  .benefits .continued { padding-left: 12px; }
  .benefits .continued::before { content: ""; }

  .processing {
    position: absolute; left: 340px; top: 132px; width: 183px;
    font-size: 23px; line-height: 31px; color: var(--ink);
    font-variant-numeric: slashed-zero;
  }
  .processing-row { display: flex; justify-content: space-between; }
  .processing-label { font-weight: 700; }
  .processing-value { font-weight: 500; }

  .pharmacist-note {
    position: absolute; left: 0; right: 0; top: 282px;
    text-align: center; color: var(--muted); font-size: 13px; line-height: 16px;
  }
  .pharmacist-note .heading { font-weight: 700; margin-bottom: 5px; }
</style>
</head>
<body>
  <section class="card card-front">
    <svg class="card-shapes" viewBox="0 0 613 351" aria-hidden="true">
      <polygon class="shape-navy" points="121,0 613,0 613,89 498,186"/>
      <polygon class="shape-red" points="304,351 613,89 613,351"/>
    </svg>
    <p class="pricing-note">Check Current Pricing on our Website</p>
    <p class="brand-name">MedPath.com</p>
    <p class="tagline">Discounting Prescription Drug Card</p>
  </section>

  <section class="card card-back">
    <svg class="card-shapes" viewBox="0 0 613 351" aria-hidden="true">
      <polygon class="shape-red" points="0,0 139,0 0,107"/>
      <polygon class="shape-navy" points="139,0 613,0 613,118"/>
    </svg>
    <p class="brand-name">MedPath.com</p>
    <ul class="benefits">
      <li>Save up to 99%</li>
      <li>100% HIPAA Compliant</li>
      <li>Lower Price Guarantee</li>
      <li>Covers 90 Days Supply</li>
      <li class="continued">&amp; Pet Meds</li>
    </ul>
    <div class="processing">
      <div class="processing-row"><span class="processing-label">BIN:</span><span class="processing-value">000000</span></div>
      <div class="processing-row"><span class="processing-label">ID:</span><span class="processing-value">RX0000</span></div>
      <div class="processing-row"><span class="processing-label">PCN:</span><span class="processing-value">RX000</span></div>
      <div class="processing-row"><span class="processing-label">GROUP:</span><span class="processing-value">RX0000</span></div>
    </div>
    <div class="pharmacist-note">
      <p class="heading">ATTENTION PHARMACIST</p>
      <p>If you are unable to process a prescription through our program</p>
      <p>please call (866)-555-0142</p>
    </div>
  </section>
</body>
</html>
```